Ledgerova - Corporate Overview - 2014

We need our Corporate Overview PPT for circulation to our clients urgently. We are an Accounting Outsourcing Company, having our Real Estate Funding arm based out of Goa, India.
I can share our draft PPT prepared in-house for further details.
The text may undergo a change, but need to make the PPT very insightful and corporate.
The designing should be based based out of our unique logo and should have our own identity.

Target Market(s)

REAL ESTATE COMPANIES requiring funding

Industry/Entity Type

Real Estate

Font styles to use
Serif

Requirements
Must have
• Real estate related high definition pictures
Nice to have
• Logo matching designs

```html
<!DOCTYPE html>
<html lang="en">
<head>
<meta charset="utf-8">
<title>Ledgerova – Corporate Overview 2014</title>
<link href="https://fonts.googleapis.com/css2?family=Bebas+Neue&family=Open+Sans:wght@300;400;600;700&display=swap" rel="stylesheet">
<style>
:root{
  --stage:#000;
  --paper:#fafafa;
  --ink:#2b2b2b;
  --rule:#c9c9c9;
  --purple:#4b2a7a;
  --purple-mid:#6a4a9a;
  --purple-pale:#b9a7d3;
  --tile:#6b6b6b;
  --sky-top:#2c5fa6;
  --sky-mid:#8fb2da;
  --glass-dark:#1a2a44;
}
*{margin:0;padding:0;box-sizing:border-box}
html,body{width:1200px;height:1000px;overflow:hidden;background:var(--stage)}
body{position:relative;font-family:"Open Sans",Arial,sans-serif;color:var(--ink)}
.showcase-title{position:absolute;left:28px;top:20px;font-family:"Bebas Neue",Impact,sans-serif;font-weight:400;font-size:44px;line-height:1;color:#fff;letter-spacing:.3px}
.slide{position:absolute;width:374px;height:210px;background:var(--paper);overflow:hidden}
.col-1{left:22px}.col-2{left:414px}.col-3{left:807px}
.row-1{top:80px}.row-2{top:310px}.row-3{top:538px}.row-4{top:766px}
.photo{position:absolute}
.photo-sky{background:linear-gradient(160deg,var(--sky-mid) 0%,var(--sky-top) 45%,var(--glass-dark) 100%)}
.photo-glass{background:linear-gradient(200deg,#cfe0f2 0%,#4c7fbf 40%,#1d3b68 100%)}
.photo-dark{background:linear-gradient(180deg,#263e66 0%,#3e5f8e 40%,#9db1c9 62%,#304c78 100%)}
.slide-title{position:absolute;left:32px;top:16px;font-weight:400;font-size:12px;letter-spacing:.6px;color:#444;padding:0 24px 3px 0;border-bottom:1px solid #9a9a9a;white-space:nowrap}
.slide-title.numbered{left:28px;display:flex;align-items:center;gap:8px}
.badge{display:inline-flex;align-items:center;justify-content:center;width:13px;height:13px;border-radius:50%;background:var(--purple-pale);color:#fff;font-size:8px;font-weight:700}
.on-photo{color:#fff;border-bottom-color:rgba(255,255,255,.6)}
.body{position:absolute;font-size:5px;line-height:1.5;color:var(--ink);text-align:justify}
.body p+p{margin-top:5px}
.footer-rule{position:absolute;left:18px;right:22px;top:186px;height:1px;background:var(--rule)}
.mini-brand{position:absolute;left:18px;top:193px;font-size:5.5px;font-weight:700;color:var(--purple);letter-spacing:.3px}
.page-no{position:absolute;right:14px;top:194px;font-size:6px;color:#666}
.cover-brand{position:absolute;left:0;right:0;top:80px;text-align:center}
.cover-brand .name{font-size:15px;font-weight:400;color:var(--purple);letter-spacing:.5px;line-height:1}
.cover-brand .tag{font-size:5px;color:var(--purple-mid);letter-spacing:.6px;margin-top:3px}
.cover-date{position:absolute;left:0;right:0;top:196px;text-align:center;font-size:6px;color:var(--purple-mid)}
.intro-panel{position:absolute;left:0;top:85px;width:166px;height:64px;background:rgba(215,215,215,.88);padding:8px 8px 6px 12px;font-size:5px;line-height:1.5;color:#333}
.client{position:absolute;width:76px;height:52px;background:var(--tile)}
.client .label{position:absolute;left:0;right:0;bottom:0;height:11px;background:var(--purple);color:#fff;font-size:5px;padding-left:12px;line-height:11px}
.client .label::before{content:"";position:absolute;left:0;top:0;width:6px;height:11px;background:var(--purple-pale)}
.bullets{list-style:none;position:absolute;font-size:5px;color:var(--ink)}
.bullets li{position:relative;padding-left:9px;margin-bottom:11px}
.bullets li::before{content:"+";position:absolute;left:0;top:-1.5px;color:var(--purple-mid);font-weight:700;font-size:7px}
.band{position:absolute;left:0;right:0;background:rgba(236,236,236,.88);text-align:center;color:#333}
.quote{font-size:8px;line-height:1.45;letter-spacing:.2px}
.offer-head{font-size:7.5px;line-height:1.35;letter-spacing:.2px}
.offer-list{display:grid;grid-template-columns:172px 150px;text-align:left;font-size:5.5px;row-gap:9px;margin:8px 0 0 38px}
.thanks{position:absolute;left:0;right:0;top:70px;text-align:center}
.thanks h2{font-size:12px;font-weight:700;color:var(--purple);letter-spacing:.3px}
.thanks .line{font-size:4.6px;color:#555;line-height:1.6}
.thanks .line.brand{color:var(--purple);font-weight:700;margin-top:2px}
.thanks .line.tag{color:var(--purple-mid)}
.centered-brand{left:158px}
</style>
</head>
<body>

<h1 class="showcase-title">FULLY EDITABLE WITH MOTION EFFECTS.</h1>

<section class="slide col-1 row-1">
  <div class="cover-brand">
    <div class="name">LEDGEROVA</div>
    <div class="tag">CAPITAL &amp; ADVISORY</div>
  </div>
  <p class="cover-date">Corporate overview / 2014</p>
</section>

<section class="slide col-2 row-1">
  <div class="photo photo-sky" style="left:0;top:0;width:374px;height:210px" role="img" aria-label="Glass skyscrapers rising into a blue sky with white clouds"></div>
  <div class="intro-panel">We fund real estate growth with clear finance, steady advice and a partner who stays with each project from land to launch. Our team joins accounting rigour with market insight, helping developers plan well, raise capital on fair terms and report results with full confidence.</div>
</section>

<section class="slide col-3 row-1">
  <h2 class="slide-title">WHAT WE DO ?</h2>
  <div class="photo photo-glass" style="left:26px;top:40px;width:324px;height:70px" role="img" aria-label="Wide view of glass office towers against the sky"></div>
  <div class="body" style="left:38px;top:117px;width:300px">
    <p>Ledgerova offers accounting outsourcing and real estate funding to developers across the region. We guide clients through corporate planning, project planning, equity and debt syndication and land purchase, with care and clear reporting at every step, so each decision rests on sound numbers and honest advice.</p>
    <p>Our team pairs local market knowledge with strict financial discipline. We build structures that last, keep lenders and investors informed, and stay close to every project until the final unit is sold, giving each client one trusted partner for funding, accounts and growth.</p>
  </div>
  <div class="footer-rule"></div>
  <div class="mini-brand">LEDGEROVA</div>
  <span class="page-no">3</span>
</section>

<section class="slide col-1 row-2">
  <h2 class="slide-title">OUR CLIENTS</h2>
  <div class="client" style="left:45px;top:48px"><div class="label">Logoname</div></div>
  <div class="client" style="left:148px;top:48px"><div class="label">Logoname</div></div>
  <div class="client" style="left:251px;top:48px"><div class="label">Logoname</div></div>
  <div class="client" style="left:45px;top:110px"><div class="label">Logoname</div></div>
  <div class="client" style="left:148px;top:110px"><div class="label">Logoname</div></div>
  <div class="client" style="left:251px;top:110px"><div class="label">Logoname</div></div>
  <div class="footer-rule"></div>
  <div class="mini-brand">LEDGEROVA</div>
  <span class="page-no">4</span>
</section>

<section class="slide col-2 row-2">
  <h2 class="slide-title">360º SERVICES FOR REAL ESTATE INDUSTRY</h2>
  <svg style="position:absolute;left:0;top:0" width="374" height="210" viewBox="0 0 374 210" font-family="Open Sans, Arial, sans-serif">
    <circle cx="182" cy="104" r="52" fill="none" stroke="#4b2a7a" stroke-width="1.5"/>
    <g fill="#fff" stroke="#4b2a7a" stroke-width="2.5">
      <circle cx="182" cy="58" r="20"/><circle cx="228" cy="92" r="20"/><circle cx="212" cy="150" r="20"/><circle cx="152" cy="150" r="20"/><circle cx="136" cy="92" r="20"/>
    </g>
    <g fill="#b9a7d3">
      <circle cx="199" cy="44" r="6"/><circle cx="246" cy="84" r="6"/><circle cx="234" cy="155" r="6"/><circle cx="130" cy="156" r="6"/><circle cx="117" cy="82" r="6"/>
    </g>
    <g fill="#fff" font-size="7" font-weight="700" text-anchor="middle">
      <text x="199" y="46.5">1</text><text x="246" y="86.5">2</text><text x="234" y="157.5">3</text><text x="130" y="158.5">4</text><text x="117" y="84.5">5</text>
    </g>
    <g fill="#222" font-size="5" font-weight="600" text-anchor="middle">
      <text x="182" y="56">Corporate</text><text x="182" y="62">Planing</text>
      <text x="228" y="90">Project</text><text x="228" y="96">Planing</text>
      <text x="212" y="148">Equity</text><text x="212" y="154">Syndication</text>
      <text x="152" y="148">Debt</text><text x="152" y="154">Syndication</text>
      <text x="136" y="84">Land</text><text x="136" y="90">Acquistion</text><text x="136" y="96">Support</text>
    </g>
  </svg>
  <div class="footer-rule"></div>
  <div class="mini-brand">LEDGEROVA</div>
  <span class="page-no">5</span>
</section>

<section class="slide col-3 row-2">
  <h2 class="slide-title numbered"><span class="badge">1</span>CORPORATE PLANNING</h2>
  <div class="body" style="left:32px;top:50px;width:182px">
    <p>We shape the financial and legal base of your group so that growth stays orderly, funded and easy to manage. From entity design to team mentoring, we set the structure that lets every new project start on firm ground.</p>
  </div>
  <ul class="bullets" style="left:44px;top:96px">
    <li>Creating long term Financial and legal structure of group</li>
    <li>Planning for setting up SPVs, Limited</li>
    <li>Mentoring and Trening Key Management Team</li>
    <li>Continuous Trainning to Staff for better efficiency</li>
  </ul>
  <div class="photo photo-glass" style="left:224px;top:44px;width:100px;height:130px" role="img" aria-label="Tall glass tower seen from below"></div>
  <div class="footer-rule"></div>
  <div class="mini-brand">LEDGEROVA</div>
  <span class="page-no">6</span>
</section>

<section class="slide col-1 row-3">
  <div class="photo photo-dark" style="left:0;top:0;width:374px;height:210px" role="img" aria-label="Dark glass skyscrapers seen from street level"></div>
  <h2 class="slide-title numbered on-photo"><span class="badge">1</span>PROJECT PLANNING</h2>
  <div class="band quote" style="top:75px;height:64px;padding-top:18px">IF YOU DON'T KNOW WHERE YOU ARE GOING,<br>IT IS DIFFICULT TO GET THERE.</div>
</section>

<section class="slide col-2 row-3">
  <div class="photo photo-dark" style="left:0;top:0;width:374px;height:210px" role="img" aria-label="Dark glass skyscrapers seen from street level"></div>
  <h2 class="slide-title numbered on-photo"><span class="badge">1</span>PROJECT PLANNING</h2>
  <div class="band" style="top:64px;height:92px;padding-top:7px">
    <div class="offer-head">WE HELP ORGANIZATIONS SET GOAL'S AND HELP THEM CHAIK OUT STRATEGIES<br>TO ARCHIEVE THEM. SOME OF KEY PROJECT PLANNING OFTERINGS INCLUDES:</div>
    <div class="offer-list">
      <span>- Project peasibility report</span><span>- Control</span>
      <span>- Financial Monitoring of the project</span><span>- Managements Reports and Internal</span>
      <span>- Cost Monitoing and Inventory</span><span>- Audit</span>
    </div>
  </div>
</section>

<section class="slide col-3 row-3">
  <h2 class="slide-title numbered"><span class="badge">3</span>EQUITY SYNDICATION</h2>
  <div class="photo photo-glass" style="left:35px;top:55px;width:155px;height:103px" role="img" aria-label="Blue glass facade of an office tower"></div>
  <div class="body" style="left:205px;top:58px;width:140px">
    <p>We bring investors and developers together, pooling equity for projects that need a strong and patient capital base. Each partner is chosen for fit, so goals, timelines and risk appetite stay aligned from the first meeting to exit.</p>
    <p>Every deal is checked, priced and reported with care. Investors receive clear updates on progress, cost and returns, so partners always know where their funds stand.</p>
  </div>
  <div class="footer-rule"></div>
  <div class="mini-brand">LEDGEROVA</div>
  <span class="page-no">9</span>
</section>

<section class="slide col-1 row-4">
  <h2 class="slide-title numbered"><span class="badge">4</span>DEBT SYNDICATION</h2>
  <div class="photo photo-glass" style="left:38px;top:44px;width:90px;height:60px" role="img" aria-label="Glass towers under a cloudy sky"></div>
  <div class="photo photo-glass" style="left:142px;top:44px;width:90px;height:60px" role="img" aria-label="Office towers against a blue sky"></div>
  <div class="photo photo-sky" style="left:245px;top:44px;width:90px;height:60px" role="img" aria-label="Skyscraper rising into clouds"></div>
  <div class="body" style="left:38px;top:108px;width:90px"><p>We arrange debt from banks and lenders, matched to the cash flow and timeline of each project. Our team prepares papers, negotiates fair terms and tracks every drawdown.</p></div>
  <div class="body" style="left:142px;top:108px;width:90px"><p>We arrange debt from banks and lenders, matched to the cash flow and timeline of each project. Our team prepares papers, negotiates fair terms and tracks every drawdown.</p></div>
  <div class="body" style="left:245px;top:108px;width:90px"><p>We arrange debt from banks and lenders, matched to the cash flow and timeline of each project. Our team prepares papers, negotiates fair terms and tracks every drawdown.</p></div>
  <div class="footer-rule"></div>
  <div class="mini-brand">LEDGEROVA</div>
  <span class="page-no">10</span>
</section>

<section class="slide col-2 row-4">
  <h2 class="slide-title numbered"><span class="badge">5</span>LAND ACQUISITION</h2>
  <div class="photo photo-sky" style="left:32px;top:44px;width:88px;height:130px" role="img" aria-label="Tall glass tower against a blue sky"></div>
  <div class="body" style="left:134px;top:48px;width:216px">
    <p>We help find, assess and secure land with clear title, fair price and a sound plan for future development. Our team studies location, access, zoning and demand before any offer is made, and handles due diligence with legal partners so the purchase closes smoothly.</p>
  </div>
  <div class="body" style="left:140px;top:110px;width:200px;text-align:left;line-height:1">
    <p>- Title checks and legal review of each parcel</p>
    <p style="margin-top:14px">- Site survey support</p>
    <p style="margin-top:14px">- Price and zoning advice for each plot on offer</p>
  </div>
  <div class="footer-rule"></div>
  <div class="mini-brand">LEDGEROVA</div>
  <span class="page-no">11</span>
</section>

<section class="slide col-3 row-4">
  <div class="thanks">
    <h2>THANK YOU</h2>
    <p class="line brand">LEDGEROVA</p>
    <p class="line tag">CAPITAL &amp; ADVISORY</p>
    <p class="line">Phone: 0000000000</p>
    <p class="line">Mobile: 000000000</p>
    <p class="line">000000@000000.com</p>
    <p class="line">www.ledgerova.com</p>
  </div>
  <div class="mini-brand centered-brand">LEDGEROVA</div>
</section>

</body>
</html>
```